Creative, fresh business card design for Orrin Linings

We need a fresh, creative business card design for Orrin Linings. We are the manufacturer of Orrin Linings in Australia. Wall panels are 2400 x 1200mm panels made from MDF and feature 3D patterns on the face of the panel. The colours to be used are green, silver/grey and white RGB
Red 187
Green 207
Blue 65.

An idea is to possibly use a watermark of one of our designs as a background (like on the "Ferns" design on the left hand side of page 2 of our brochure).

Target Market(s)

Interior designers, architects, builders and home renovators

Industry/Entity Type

Business

Contact Information for Business Card

Details to go on the card are:
Our logo (attached),
Slogan: "Decorative panels for interiors and exteriors",
Contact name,
Position,
Mobile phone number,
Business address,
Business phone,
Business fax,
Website and
Email address.

I have attached a few images of our panels and our brochure for reference.

The colours of the business card should feature our logo colours which are: RGB
Red 187
Green 207
Blue 65

Requirements
Must have
• Very modern fonts and design. Some of the designs shown especially the "Weave" design which is a popular design.
Nice to have
• Creative but simple design. Very contemporary.
Should not have
• Anything ornate or old fashioned.

```html
<!DOCTYPE html>
<html lang="en">
<head>
<meta charset="utf-8">
<title>Orrin Linings – Business Card</title>
<link rel="stylesheet" href="https://fonts.googleapis.com/css2?family=Exo+2:wght@500&family=Raleway:wght@400;500;700;800&display=swap">
<style>
  :root {
    --brand-green: #bbcf41;
    --silver: #9a9b9e;
    --ink: #555659;
    --ink-soft: #5e5f62;
    --panel-white: #ffffff;
    --panel-shade: #e6e6e6;
    --page: #ebe8e3;
  }
  html, body {
    margin: 0;
    width: 1200px;
    height: 709px;
    overflow: hidden;
    background: var(--page);
  }
  .card {
    position: absolute;
    left: 80px;
    top: 57px;
    width: 1040px;
    height: 594px;
    border-radius: 42px;
    overflow: hidden;
    background: var(--brand-green);
    box-shadow: 0 10px 28px rgba(0,0,0,0.18);
    font-family: "Raleway", sans-serif;
    color: var(--ink);
  }
  .card-shapes { position: absolute; inset: 0; }
  .brand {
    position: absolute;
    left: 40px;
    width: 360px;
    top: 196px;
    display: flex;
    align-items: center;
    justify-content: center;
    gap: 14px;
  }
  .brand-square {
    width: 30px;
    height: 30px;
    background: var(--panel-white);
  }
  .brand-name {
    font-weight: 700;
    font-size: 40px;
    color: var(--ink);
    white-space: nowrap;
  }
  .slogan {
    position: absolute;
    left: 40px;
    width: 360px;
    top: 320px;
    text-align: center;
    font-weight: 500;
    font-size: 22px;
    line-height: 29px;
    color: var(--ink-soft);
  }
  .person {
    position: absolute;
    left: 30px;
    width: 380px;
    top: 446px;
    text-align: center;
  }
  .person-name {
    font-weight: 800;
    font-size: 32px;
    letter-spacing: 0.2px;
    color: var(--ink);
  }
  .person-rule {
    height: 2px;
    margin: 8px 34px 10px;
    background: linear-gradient(90deg, transparent, rgba(255,255,255,0.85), transparent);
  }
  .person-role {
    font-weight: 400;
    font-size: 29px;
    color: var(--ink-soft);
  }
  .contact {
    position: absolute;
    display: flex;
    align-items: center;
    font-family: "Exo 2", sans-serif;
    font-weight: 500;
    font-size: 33px;
    line-height: 42px;
    color: var(--ink);
    white-space: nowrap;
  }
  .contact-icon {
    width: 30px;
    height: 30px;
    fill: var(--ink);
    flex: none;
  }
  .contact-phone   { left: 440px; top: 74px; }
  .contact-address { left: 470px; top: 152px; }
  .contact-fax     { left: 498px; top: 285px; }
  .contact-web     { left: 518px; top: 362px; }
  .contact-email   { left: 550px; top: 446px; }
  .contact-phone .contact-icon   { margin-right: 26px; }
  .contact-address .contact-icon { margin-right: 28px; }
  .contact-fax .contact-icon     { margin-right: 24px; }
  .contact-web .contact-icon     { margin-right: 24px; }
  .contact-email .contact-icon   { margin-right: 28px; }
</style>
</head>
<body>
  <div class="card">
    <svg class="card-shapes" viewBox="0 0 1040 594" width="1040" height="594" aria-hidden="false">
      <defs>
        <linearGradient id="panelTexture" x1="0" y1="0" x2="1" y2="1">
          <stop offset="0" stop-color="#f4f4f4"/>
          <stop offset="0.5" stop-color="#fbfbfb"/>
          <stop offset="1" stop-color="#ececec"/>
        </linearGradient>
      </defs>
      <path class="silver-edge" fill="var(--silver)"
            d="M362 0 L1040 0 L1040 594 L560 594 Q520 594 508 562 L352 30 Q346 0 372 0 Z"/>
      <path class="panel-face" fill="url(#panelTexture)" role="img"
            aria-label="Soft white embossed 3D wall panel texture"
            d="M378 0 L1040 0 L1040 594 L576 594 Q538 594 526 562 L370 30 Q364 0 390 0 Z"/>
    </svg>

    <div class="brand">
      <span class="brand-square"></span>
      <span class="brand-name">Orrin Linings</span>
    </div>
    <p class="slogan" style="margin:0">Decorative panels for<br>interiors and exteriors</p>

    <div class="person">
      <div class="person-name">CALDER R VOSS</div>
      <div class="person-rule"></div>
      <div class="person-role">Executive Director</div>
    </div>

    <div class="contact contact-phone">
      <svg class="contact-icon" viewBox="0 0 24 24"><path d="M9 1h8a2 2 0 0 1 2 2.4l-3.2 17.2A2 2 0 0 1 13.8 22H6a2 2 0 0 1-2-2.4L7.2 2.6A2 2 0 0 1 9 1zm.2 2L6 20h7.8L17 3zM10 18.2h2.4v1.2H10z"/></svg>
      <span>800-413-7290 / 41-7702</span>
    </div>

    <div class="contact contact-address">
      <svg class="contact-icon" viewBox="0 0 24 24"><path d="M12 1.5a7 7 0 0 0-7 7c0 5.2 7 14 7 14s7-8.8 7-14a7 7 0 0 0-7-7zm0 4a2.3 2.3 0 1 1 0 4.6 2.3 2.3 0 0 1 0-4.6zm-3.6 8.6c.6-1.6 2-2.5 3.6-2.5s3 .9 3.6 2.5L12 18.3z"/></svg>
      <span>48 Harlow St. Kestrel Vale<br>Melbourne 3187</span>
    </div>

    <div class="contact contact-fax">
      <svg class="contact-icon" viewBox="0 0 24 24"><path d="M6 2h9l3 3v4h2a2 2 0 0 1 2 2v9a2 2 0 0 1-2 2H8a2 2 0 0 1-2-2zm2 2v5h8V6h-2V4zM3 8h2v14H3a1 1 0 0 1-1-1V9a1 1 0 0 1 1-1zm7 4v2h2v-2zm4 0v2h2v-2zm4 0v2h2v-2zm-8 4v2h2v-2zm4 0v2h2v-2zm4 0v2h2v-2z"/></svg>
      <span>Fax# 800-413-7291</span>
    </div>

    <div class="contact contact-web">
      <svg class="contact-icon" viewBox="0 0 24 24"><path d="M12 1.5a10.5 10.5 0 1 0 0 21 10.5 10.5 0 0 0 0-21zm-1.5 2.6c-.5 1.3-2.2 1.8-2.6 3.3-.4 1.6 1.4 2 2.4 3 1 1 .2 2.6 1.2 3.6.9.9 2.4.6 2.8 2 .3 1.1-.5 2.5-1 3.6A8.5 8.5 0 0 1 4.4 8.2c1 .6 1.7 1.6 2.8 1.2zM16.5 5a8.5 8.5 0 0 1 3 9.2c-.9-.6-1.6-1.8-2.7-1.6-1.2.2-1.8-1-1.4-2 .5-1.4 2-2 1.8-3.5-.1-.8-.5-1.5-.7-2.1z"/></svg>
      <span>www.OrrinLinings.com</span>
    </div>

    <div class="contact contact-email">
      <svg class="contact-icon" viewBox="0 0 24 24"><path d="M2 5h20v2l-10 6L2 7zm0 4.3 10 6 10-6V19H2z"/></svg>
      <span>info@OrrinLinings.com</span>
    </div>
  </div>
</body>
</html>
```